I need a business card representing my company, VELDRA, it's an artist management and design company. Complete name is "VELDRA Artist Mgmt. + Design Co." I need it to be world class and very appealing, sophisticated and artistically unique.
Updates

Posted an updated Brief please see. I need a business card representing my company, VELDRA, it's an artist management and design company. Complete name is "VELDRA Artist Mgmt. + Design Co." I need it to be world class and very appealing, sophisticated and artistically unique.

Designs look the same

Designs look the same

Target Market(s)

Advertisers, Entertainment Companies, Commercial companies

Industry/Entity Type

Advertising

Contact Information for Business Card

I need a business card representing my company, VELDRA, it's an artist management and design company. Complete name is "VELDRA Artist Mgmt. + Design Co." I need it to be world class and very appealing, sophisticated and artistically unique. One side can be VELDRA Artist Mgmt. + Design Co. and the other my name, Teodoro Lindqvist, my contact telephone: 412.638.2957, email veldraartist@plumora.net, my address: 3264 Harwell Ave. #517 Miami, FL 33184

Font styles to use
Other font styles liked:
• Calibri

Colors
ffffff
0455a3
f37122

Requirements
Must have
• "VELDRA" stand out bigger than the rest of the text.
Nice to have
• Name "VELDRA" can be centered on one side or in the corner or along side edges, just need something cool and different.
Should not have
• I am open just try to keep it clean looking

```html
<!DOCTYPE html>
<html lang="en">
<head>
<meta charset="utf-8">
<title>VELDRA Artist Management + Design Co. – Business Card</title>
<link rel="stylesheet" href="https://fonts.googleapis.com/css2?family=Montserrat:ital,wght@0,300;0,400;0,700;1,800&display=swap">
<style>
  :root {
    --page: #ffffff;
    --violet-light: #8a4fb8;
    --violet: #7a2fa8;
    --violet-deep: #4e1a6e;
    --ice: #e4f2fb;
    --white: #ffffff;
    --accent-blue: #1aa3e8;
  }
  * { box-sizing: border-box; margin: 0; padding: 0; }
  html, body {
    width: 1200px; height: 1200px; overflow: hidden;
    background: var(--page);
    font-family: "Montserrat", sans-serif;
  }
  .card {
    position: absolute;
    width: 840px; height: 480px;
    overflow: hidden;
    color: var(--white);
  }
  .card--front { left: 170px; top: 70px; }
  .card--back  { left: 173px; top: 586px; }
  .card__texture {
    position: absolute; inset: 0;
    background:
      radial-gradient(ellipse at 30% 20%, rgba(255,255,255,0.12), transparent 60%),
      linear-gradient(180deg, var(--violet-light) 0%, var(--violet) 55%, var(--violet-deep) 100%);
  }
  .wordmark {
    position: absolute;
    font-weight: 400;
    color: var(--ice);
    letter-spacing: -0.02em;
    line-height: 1;
    white-space: nowrap;
  }
  .tagline {
    position: absolute;
    font-weight: 300;
    white-space: nowrap;
    line-height: 1;
  }
  .tagline .plus { color: var(--accent-blue); font-weight: 700; }

  .card--front .wordmark { left: 70px; top: 70px; font-size: 220px; }
  .card--front .tagline  { left: 178px; top: 312px; font-size: 35px; }

  .services {
    position: absolute; left: 0; top: 382px; width: 100%; height: 60px;
  }
  .service-icon {
    position: absolute; width: 58px; height: 58px;
    fill: none; stroke: var(--white); stroke-width: 4; stroke-linecap: round; stroke-linejoin: round;
  }
  .service-icon .solid { fill: var(--white); stroke: none; }
  .service-icon--music  { left: 62px; }
  .service-icon--home   { left: 285px; }
  .service-icon--brush  { left: 506px; }
  .service-icon--sewing { left: 729px; }

  .card--back .wordmark { left: 100px; top: 70px; font-size: 168px; }
  .card--back .tagline  { left: 225px; top: 222px; font-size: 28px; }

  .contact { position: absolute; top: 304px; font-size: 27px; line-height: 36px; }
  .contact--address { left: 59px; font-weight: 300; }
  .contact--lines { left: 526px; font-weight: 300; }
  .contact__row { display: flex; white-space: nowrap; }
  .contact__label { width: 89px; font-weight: 800; font-style: italic; }
  .contact__label--plain { font-style: normal; }
  .contact__site { font-weight: 700; }
</style>
</head>
<body>

<section class="card card--front" aria-label="Business card front">
  <div class="card__texture" role="img" aria-label="Purple painted brush-stroke texture"></div>
  <div class="wordmark">veldra</div>
  <div class="tagline">Artist Management <span class="plus">+</span> Design Co.</div>
  <div class="services">
    <svg class="service-icon service-icon--music" viewBox="0 0 60 60" aria-label="Music">
      <ellipse class="solid" cx="14" cy="48" rx="9" ry="7"/>
      <ellipse class="solid" cx="42" cy="44" rx="9" ry="7"/>
      <path d="M21 47V10l28-6v40"/>
      <path d="M21 18l28-6"/>
    </svg>
    <svg class="service-icon service-icon--home" viewBox="0 0 60 60" aria-label="Interior design">
      <path d="M4 26L30 4l26 22"/>
      <path d="M10 22v34h40V22"/>
      <path d="M18 44v-8h24v8z"/>
      <path d="M20 36v-6h20v6"/>
    </svg>
    <svg class="service-icon service-icon--brush" viewBox="0 0 60 60" aria-label="Fine art">
      <path class="solid" d="M56 4L26 36l-4-3z"/>
      <path class="solid" d="M20 35c-7 0-10 6-11 12-1 5-4 7-6 9 10 1 20-3 22-14z"/>
    </svg>
    <svg class="service-icon service-icon--sewing" viewBox="0 0 60 60" aria-label="Fashion design">
      <path d="M20 4h20"/>
      <path d="M20 4c-8 6-6 18-4 26-4 6-4 12-2 16h32c2-4 2-10-2-16 2-8 4-20-4-26"/>
      <rect x="10" y="42" width="44" height="10" rx="1"/>
      <path d="M18 42v5M24 42v4M30 42v5M36 42v4M42 42v5"/>
      <path d="M30 52v6"/>
    </svg>
  </div>
</section>

<section class="card card--back" aria-label="Business card back">
  <div class="card__texture" role="img" aria-label="Purple painted brush-stroke texture"></div>
  <div class="wordmark">veldra</div>
  <div class="tagline">Artist Management <span class="plus">+</span> Design Co.</div>

  <address class="contact contact--address" style="font-style:normal">
    <div>3264 Harwell Avenue</div>
    <div>Studio 517</div>
    <div>Miami, Florida 33184</div>
    <div>tlindqvist@veldraart.com</div>
  </address>

  <div class="contact contact--lines">
    <div class="contact__row"><span class="contact__label">Office</span><span>412.638.2950</span></div>
    <div class="contact__row"><span class="contact__label">Direct</span><span>412.638.2957</span></div>
    <div class="contact__row"><span class="contact__label contact__label--plain">Fax</span><span>412.638.2958</span></div>
    <div class="contact__row"><span class="contact__site">veldraart.com</span></div>
  </div>
</section>

</body>
</html>
```